Course Graduation Certificate

This project is not for a flyer but instead for the creation of a course graduation certificate. The final certificate needs to include the Marlowe Summit Aviation Academy logo and the text stating as follows:
Certifies that ___________________________ has satisfactorily completed the course of _______________________________ on ________________________________
I would also like to include some type of gold seal of completion as well as a place to sign my name and credentials at the bottom of the certificate
I have included the Marlowe Summit Aviation Academy logo as well as three other certificate examples for you to work from.
Target Market(s)
Students completing a certification course and receiving a certificate
Look and feel

```html
<!DOCTYPE html>
<html lang="en">
<head>
<meta charset="utf-8">
<title>Course Graduation Certificate – Marlowe Summit Aviation Academy</title>
<link href="https://fonts.googleapis.com/css2?family=Barlow:wght@400;600&family=UnifrakturMaguntia&display=swap" rel="stylesheet">
<style>
  :root {
    --backdrop: #e9e9e9;
    --paper: #ffffff;
    --royal-blue: #1f58b0;
    --ornament-blue: #3b6cbd;
    --ornament-light: #b9cdec;
    --ink: #1a1a1a;
    --rule: #222222;
    --gold-light: #f6dc8a;
    --gold-mid: #d7a83a;
    --gold-dark: #a9791c;
  }
  html, body {
    margin: 0;
    padding: 0;
    width: 1200px;
    height: 1200px;
    overflow: hidden;
    background: var(--backdrop);
  }
  .canvas {
    position: relative;
    width: 1200px;
    height: 1200px;
  }
  .certificate {
    position: absolute;
    left: 81px;
    top: 200px;
    width: 1038px;
    height: 800px;
    background: var(--paper);
    font-family: "Barlow", Arial, sans-serif;
    color: var(--ink);
  }
  .border-band {
    position: absolute;
    left: 34px;
    top: 59px;
    width: 972px;
    height: 679px;
    box-sizing: border-box;
    border: 15px solid var(--ornament-light);
    outline: 2px solid var(--ornament-blue);
    outline-offset: -2px;
  }
  .border-band::after {
    content: "";
    position: absolute;
    inset: 2px;
    border: 2px solid var(--ornament-blue);
  }
  .corner-ornament {
    position: absolute;
    width: 138px;
    height: 125px;
  }
  .corner-ornament--top-left {
    left: 50px; top: 75px;
    border-radius: 0 0 100% 0;
    background: radial-gradient(circle at 0 0, var(--ornament-blue) 0%, var(--ornament-light) 70%, rgba(185,205,236,0) 100%);
  }
  .corner-ornament--top-right {
    left: 850px; top: 75px;
    border-radius: 0 0 0 100%;
    background: radial-gradient(circle at 100% 0, var(--ornament-blue) 0%, var(--ornament-light) 70%, rgba(185,205,236,0) 100%);
  }
  .corner-ornament--bottom-left {
    left: 50px; top: 575px;
    border-radius: 0 100% 0 0;
    background: radial-gradient(circle at 0 100%, var(--ornament-blue) 0%, var(--ornament-light) 70%, rgba(185,205,236,0) 100%);
  }
  .corner-ornament--bottom-right {
    left: 850px; top: 575px;
    border-radius: 100% 0 0 0;
    background: radial-gradient(circle at 100% 100%, var(--ornament-blue) 0%, var(--ornament-light) 70%, rgba(185,205,236,0) 100%);
  }
  .title {
    position: absolute;
    left: 0;
    top: 110px;
    width: 1038px;
    height: 140px;
  }
  .title text {
    font-family: "UnifrakturMaguntia", "Old English Text MT", serif;
    font-size: 82px;
    fill: var(--royal-blue);
  }
  .statement {
    position: absolute;
    font-size: 19px;
    line-height: 1;
    display: flex;
    align-items: flex-end;
    white-space: nowrap;
  }
  .statement .fill-line {
    display: inline-block;
    border-bottom: 1.5px solid var(--rule);
    height: 1px;
    margin-left: 4px;
    margin-bottom: 3px;
  }
  .statement--recipient { left: 163px; top: 298px; }
  .statement--recipient .fill-line { width: 576px; }
  .statement--course { left: 163px; top: 350px; }
  .statement--course .fill-line { width: 320px; }
  .statement--date { left: 163px; top: 403px; }
  .statement--date .fill-line { width: 330px; }
  .seal {
    position: absolute;
    left: 129px;
    top: 464px;
    width: 130px;
    height: 130px;
  }
  .signature-line {
    position: absolute;
    left: 616px;
    top: 510px;
    width: 303px;
    border-top: 1.5px solid var(--rule);
  }
  .signature-caption {
    position: absolute;
    left: 616px;
    top: 542px;
    width: 330px;
    text-align: center;
    font-size: 19px;
  }
  .academy-name {
    position: absolute;
    left: 319px;
    top: 600px;
    width: 400px;
    text-align: center;
    font-weight: 600;
    font-size: 26px;
    line-height: 1.15;
    color: var(--royal-blue);
  }
</style>
</head>
<body>
<div class="canvas">
  <section class="certificate">
    <div class="border-band" role="img" aria-label="Ornamental blue guilloche border frame"></div>
    <div class="corner-ornament corner-ornament--top-left" role="img" aria-label="Blue filigree corner ornament"></div>
    <div class="corner-ornament corner-ornament--top-right" role="img" aria-label="Blue filigree corner ornament"></div>
    <div class="corner-ornament corner-ornament--bottom-left" role="img" aria-label="Blue filigree corner ornament"></div>
    <div class="corner-ornament corner-ornament--bottom-right" role="img" aria-label="Blue filigree corner ornament"></div>

    <svg class="title" viewBox="0 0 1038 140" aria-label="Graduation Certificate">
      <defs>
        <path id="title-arc" d="M 130 100 Q 519 62 908 112" fill="none"/>
      </defs>
      <text text-anchor="middle"><textPath href="#title-arc" startOffset="50%">Graduation Certificate</textPath></text>
    </svg>

    <p class="statement statement--recipient" style="margin:0">Certifies that <span class="fill-line"></span></p>
    <p class="statement statement--course" style="margin:0">has satisfactorily completed the course of <span class="fill-line"></span></p>
    <p class="statement statement--date" style="margin:0">on <span class="fill-line"></span>.</p>

    <svg class="seal" viewBox="0 0 130 130" role="img" aria-label="Gold seal of completion">
      <defs>
        <linearGradient id="seal-gold" x1="0" y1="0" x2="1" y2="1">
          <stop offset="0" stop-color="var(--gold-light)"/>
          <stop offset="0.5" stop-color="var(--gold-mid)"/>
          <stop offset="1" stop-color="var(--gold-dark)"/>
        </linearGradient>
      </defs>
      <circle cx="65" cy="65" r="62" fill="url(#seal-gold)"/>
    </svg>

    <div class="signature-line"></div>
    <div class="signature-caption">Course Graduation Certificate</div>

    <div class="academy-name">Marlowe Summit<br>Aviation Academy</div>
  </section>
</div>
</body>
</html>
```